Personnel recruitment Brunnwalder GmbH

We would like to create an attractive flyer that focuses on one of our services in Saarland and Rhineland-Palatinate. The benefits for the customer should be presented.

```html
<!DOCTYPE html>
<html lang="de">
<head>
<meta charset="utf-8">
<title>Personalvermittlung – Brunnwalder GmbH</title>
<link href="https://fonts.googleapis.com/css2?family=Montserrat:wght@400;500;600;700;800&display=swap" rel="stylesheet">
<style>
  :root {
    --ink: #2a2b2e;
    --teal: #1f9c9c;
    --teal-soft: #8fd0cf;
    --teal-text: #86d3d1;
    --white: #ffffff;
  }
  * { margin: 0; padding: 0; box-sizing: border-box; }
  html, body { width: 849px; height: 1200px; overflow: hidden; background: var(--white); }
  .flyer {
    position: relative; width: 849px; height: 1200px; overflow: hidden;
    background: var(--ink); font-family: "Montserrat", sans-serif; color: var(--white);
  }
  .backdrop { position: absolute; inset: 0; }
  .brand { position: absolute; left: 63px; top: 72px; }
  .brand-name { font-weight: 700; font-size: 19px; color: var(--white); }
  .headline { position: absolute; left: 63px; top: 160px; }
  .subline { position: absolute; left: 63px; top: 213px; font-weight: 700; font-size: 17px; line-height: 22px; letter-spacing: 0.2px; white-space: nowrap; }
  .intro { position: absolute; left: 63px; top: 247px; width: 780px; font-size: 15.2px; line-height: 21.5px; color: var(--teal-text); white-space: nowrap; }
  .section-title { position: absolute; left: 63px; top: 343px; font-weight: 700; font-size: 26px; line-height: 32px; letter-spacing: 0.3px; }
  .service { position: absolute; left: 72px; display: flex; align-items: center; gap: 9px; color: var(--ink); font-size: 15.4px; line-height: 22px; letter-spacing: 0.1px; white-space: nowrap; }
  .tick { width: 28px; height: 28px; flex: none; }
  .benefits-title { position: absolute; left: 71px; top: 699px; font-weight: 700; font-size: 21.2px; line-height: 24px; letter-spacing: 0.2px; }
  .benefit { position: absolute; left: 87px; display: flex; align-items: center; gap: 9px; color: var(--teal-text); font-size: 15.6px; line-height: 22px; white-space: nowrap; }
  .contact { position: absolute; left: 89px; top: 1078px; color: var(--ink); }
  .contact-title { font-weight: 700; font-size: 11px; letter-spacing: 0.1px; }
  .contact-list { list-style: none; margin: 6px 0 0 20px; }
  .contact-list li { display: flex; align-items: center; gap: 7px; height: 17px; margin-bottom: 2px; font-weight: 700; font-size: 8.4px; }
  .contact-icon { width: 13px; height: 13px; flex: none; }
</style>
</head>
<body>
<main class="flyer">
  <svg class="backdrop" width="849" height="1200" viewBox="0 0 849 1200">
    <path d="M0 387 H772 Q792 387 796 404 V439 H0 Z" fill="var(--teal-soft)"/>
    <rect x="0" y="450" width="700" height="52" fill="var(--teal-soft)"/>
    <rect x="0" y="512" width="700" height="51" fill="var(--teal-soft)"/>
    <rect x="0" y="574" width="700" height="53" fill="var(--teal-soft)"/>
    <rect x="0" y="636" width="700" height="51" fill="var(--teal-soft)"/>
    <circle cx="711" cy="698" r="304" fill="var(--teal-soft)"/>
    <defs>
      <linearGradient id="photoTone" x1="0" y1="0" x2="0" y2="1">
        <stop offset="0" stop-color="#4563ad"/>
        <stop offset="0.45" stop-color="#6f7790"/>
        <stop offset="0.75" stop-color="#5a6356"/>
        <stop offset="1" stop-color="#cfcac3"/>
      </linearGradient>
    </defs>
    <circle cx="711" cy="698" r="289" fill="url(#photoTone)" role="img" aria-label="Foto: Firmengebäude mit Namensstele im Vorgarten"/>
    <path d="M0 1040 C200 1040 400 1110 560 1115 C700 1118 780 1100 849 1081 V1200 H0 Z" fill="var(--white)"/>
    <path d="M0 910 C250 1000 420 1060 520 1062 C650 1064 760 1010 849 951 V1081 C780 1100 700 1118 560 1115 C400 1110 200 1040 0 1040 Z" fill="var(--teal-soft)"/>
    <path d="M0 985 C200 1018 340 1068 520 1113 C360 1098 200 1040 0 1040 Z" fill="var(--ink)"/>
    <path d="M0 882 C200 960 400 1040 540 1042 C650 1044 760 1010 813 982" fill="none" stroke="var(--teal-soft)" stroke-width="4"/>
  </svg>

  <div class="brand">
    <span class="brand-name">Brunnwalder GmbH</span>
  </div>

  <svg class="headline" width="680" height="56" viewBox="0 0 680 56">
    <text x="0" y="46" textLength="665" lengthAdjust="spacingAndGlyphs" font-family="Montserrat, sans-serif" font-weight="800" font-size="56" fill="var(--teal)">PERSONALVERMITTLUNG</text>
  </svg>
  <p class="subline">EFFIZIENTE LÖSUNGEN FÜR IHRE PERSONALSUCHE</p>
  <p class="intro">Passende Mitarbeiter zu finden, stellt heute eine große Herausforderung dar.<br>Profitieren Sie von unserem Netzwerk und unserer langjährigen Erfahrung im Recruiting.<br>Entlasten Sie Ihre Abteilungsleiter und fokussieren Sie sich auf Ihr Kerngeschäft, indem Sie<br>uns mit der Personalvermittlung beauftragen.</p>

  <h2 class="section-title">UNSERE DIENSTLEISTUNG</h2>

  <div class="service" style="top:391px"><svg class="tick" viewBox="0 0 28 28"><rect x="2" y="2" width="24" height="24" rx="4" fill="none" stroke="var(--ink)" stroke-width="2.6"/><path d="M8.5 14.5 L12.5 18 L19.5 10" fill="none" stroke="var(--ink)" stroke-width="2.6" stroke-linecap="round" stroke-linejoin="round"/></svg><span>Erstellung des Anforderungsprofils mit einem<br>erfahrenen Recruiter</span></div>
  <div class="service" style="top:453px"><svg class="tick" viewBox="0 0 28 28"><rect x="2" y="2" width="24" height="24" rx="4" fill="none" stroke="var(--ink)" stroke-width="2.6"/><path d="M8.5 14.5 L12.5 18 L19.5 10" fill="none" stroke="var(--ink)" stroke-width="2.6" stroke-linecap="round" stroke-linejoin="round"/></svg><span>Gestaltung und Veröffentlichung der<br>Stellenanzeige</span></div>
  <div class="service" style="top:514px"><svg class="tick" viewBox="0 0 28 28"><rect x="2" y="2" width="24" height="24" rx="4" fill="none" stroke="var(--ink)" stroke-width="2.6"/><path d="M8.5 14.5 L12.5 18 L19.5 10" fill="none" stroke="var(--ink)" stroke-width="2.6" stroke-linecap="round" stroke-linejoin="round"/></svg><span>Bewerberselektion für jede Qualifikation<br>und Hierarchiestufe</span></div>
  <div class="service" style="top:576px"><svg class="tick" viewBox="0 0 28 28"><rect x="2" y="2" width="24" height="24" rx="4" fill="none" stroke="var(--ink)" stroke-width="2.6"/><path d="M8.5 14.5 L12.5 18 L19.5 10" fill="none" stroke="var(--ink)" stroke-width="2.6" stroke-linecap="round" stroke-linejoin="round"/></svg><span>Präsentation ausgewählter<br>Kandidaten oder aller Bewerbunge</span></div>
  <div class="service" style="top:647px"><svg class="tick" viewBox="0 0 28 28"><rect x="2" y="2" width="24" height="24" rx="4" fill="none" stroke="var(--ink)" stroke-width="2.6"/><path d="M8.5 14.5 L12.5 18 L19.5 10" fill="none" stroke="var(--ink)" stroke-width="2.6" stroke-linecap="round" stroke-linejoin="round"/></svg><span>Unterstützung beim Onboarding</span></div>

  <h2 class="benefits-title">VORTEILE DER<br>PERSONALVERMITTLUNG</h2>

  <div class="benefit" style="top:762px"><svg class="tick" viewBox="0 0 28 28"><rect x="2" y="2" width="24" height="24" rx="4" fill="none" stroke="var(--teal-soft)" stroke-width="2.6"/><path d="M8.5 14.5 L12.5 18 L19.5 10" fill="none" stroke="var(--teal-soft)" stroke-width="2.6" stroke-linecap="round" stroke-linejoin="round"/></svg><span>Zeitersparnis und Entlastung für Ihr<br>Unternehmen</span></div>
  <div class="benefit" style="top:810px;left:89px"><svg class="tick" viewBox="0 0 28 28"><rect x="2" y="2" width="24" height="24" rx="4" fill="none" stroke="var(--teal-soft)" stroke-width="2.6"/><path d="M8.5 14.5 L12.5 18 L19.5 10" fill="none" stroke="var(--teal-soft)" stroke-width="2.6" stroke-linecap="round" stroke-linejoin="round"/></svg><span>Jahrelange Erfahrung in der<br>Rekrutierung</span></div>
  <div class="benefit" style="top:858px;left:90px"><svg class="tick" viewBox="0 0 28 28"><rect x="2" y="2" width="24" height="24" rx="4" fill="none" stroke="var(--teal-soft)" stroke-width="2.6"/><path d="M8.5 14.5 L12.5 18 L19.5 10" fill="none" stroke="var(--teal-soft)" stroke-width="2.6" stroke-linecap="round" stroke-linejoin="round"/></svg><span>Größeres Bewerbernetzwerk für<br>schnellere Ergebnisse</span></div>

  <section class="contact">
    <p class="contact-title">KONTAKTIEREN SIE UNS NOCH HEUTE!</p>
    <ul class="contact-list">
      <li><svg class="contact-icon" viewBox="0 0 14 14"><circle cx="7" cy="7" r="6.2" fill="none" stroke="var(--ink)" stroke-width="1.2"/><rect x="3.6" y="4.8" width="6.8" height="4.6" fill="none" stroke="var(--ink)" stroke-width="1"/><path d="M3.6 4.8 L7 7.6 L10.4 4.8" fill="none" stroke="var(--ink)" stroke-width="1"/></svg>INFO@BRUNNWALDER.ORG</li>
      <li><svg class="contact-icon" viewBox="0 0 14 14"><circle cx="7" cy="7" r="6.2" fill="none" stroke="var(--ink)" stroke-width="1.2"/><circle cx="7" cy="7" r="3.8" fill="none" stroke="var(--ink)" stroke-width="0.9"/><ellipse cx="7" cy="7" rx="1.6" ry="3.8" fill="none" stroke="var(--ink)" stroke-width="0.9"/><path d="M3.2 7 H10.8" stroke="var(--ink)" stroke-width="0.9"/></svg>WWW.BRUNNWALDER.ORG</li>
      <li><svg class="contact-icon" viewBox="0 0 14 14"><circle cx="7" cy="7" r="6.8" fill="var(--ink)"/><path d="M4.3 3.6 L5.8 3.4 L6.5 5.4 L5.6 6.1 Q6.4 7.8 7.9 8.5 L8.6 7.6 L10.6 8.3 L10.4 9.8 Q9.8 10.6 8.6 10.4 Q4.2 9.2 3.6 5.2 Q3.5 4.1 4.3 3.6 Z" fill="var(--white)"/></svg>+00 0000 47310</li>
    </ul>
  </section>
</main>
</body>
</html>
```